Kelvora Business Card Design - double sided -plumbing local plumbing company

We have a Plumbing company where the design was create through Sketch Hive. We would now like a business card designed as well. We want it to be in the colour version of the logo.

Details below for the card.

Phone Number: 0438 615 247
Email: info@kelvoraplumbing.example.au
Website: https://kelvoraplumbing.example.au
We really want a sophisticated design that stand out from the other- informative and timeless.

Target Market(s)

local Canberra market

Industry/Entity Type

Plumbing, gas fitting, hot water

Contact Information for Business Card

Phone number, email, logo and "Supplying all your heating, cooling and hot water needs"

Requirements
Must have
• bust be colourful, must also be though about it being printed on a magnet. must Vex with the logo - I dont want the logo and information chucked onto a white canvas I would prefer it to be smooth and look purposeful

```html
<!DOCTYPE html>
<html lang="en">
<head>
<meta charset="utf-8">
<title>Kelvora Business Card</title>
<link href="https://fonts.googleapis.com/css2?family=Mulish:wght@600;700;800&display=swap" rel="stylesheet">
<style>
  :root {
    --page-bg: #ffffff;
    --blue-light: #1a7be9;
    --blue-mid: #0d55c4;
    --blue-deep: #0a3796;
    --brand-cyan: #2aaef0;
    --text-white: #ffffff;
    --icon-blue: #0b3c9c;
  }
  * { margin: 0; padding: 0; box-sizing: border-box; }
  html, body {
    width: 1200px;
    height: 1200px;
    overflow: hidden;
    background: var(--page-bg);
    font-family: "Mulish", sans-serif;
  }
  .sheet {
    position: relative;
    width: 1200px;
    height: 1200px;
  }
  .card {
    position: absolute;
    width: 716px;
    height: 410px;
    overflow: hidden;
    color: var(--text-white);
  }
  .card-front {
    left: 241px;
    top: 163px;
    background: linear-gradient(120deg, var(--blue-light) 0%, var(--blue-mid) 40%, var(--blue-deep) 100%);
  }
  .card-back {
    left: 243px;
    top: 627px;
    background: linear-gradient(120deg, var(--blue-deep) 0%, var(--blue-mid) 60%, var(--blue-light) 100%);
  }
  .card-pattern {
    position: absolute;
    inset: 0;
    background: radial-gradient(ellipse at 50% 50%, rgba(255,255,255,0.04), rgba(255,255,255,0) 70%);
  }
  .brand-name {
    position: absolute;
    left: 0;
    right: 0;
    top: 146px;
    text-align: center;
    font-weight: 800;
    font-size: 74px;
    line-height: 80px;
    letter-spacing: 3px;
    text-transform: uppercase;
    color: var(--brand-cyan);
  }
  .tagline {
    position: absolute;
    left: 0;
    right: 0;
    top: 248px;
    text-align: center;
    font-weight: 800;
    font-size: 8px;
    line-height: 12px;
    letter-spacing: 2.1px;
    text-transform: uppercase;
  }
  .contact-list {
    position: absolute;
    left: 97px;
    top: 145px;
    list-style: none;
  }
  .contact-item {
    display: flex;
    align-items: center;
    height: 39px;
    margin-bottom: 41px;
  }
  .contact-icon {
    width: 39px;
    height: 39px;
    background: var(--text-white);
    border-radius: 3px;
    display: flex;
    align-items: center;
    justify-content: center;
    flex-shrink: 0;
  }
  .contact-text {
    margin-left: 35px;
    font-weight: 600;
    font-size: 22px;
    letter-spacing: 0.8px;
  }
</style>
</head>
<body>
<main class="sheet">
  <section class="card card-front" aria-label="Business card front">
    <div class="card-pattern" role="img" aria-label="Faint repeating pattern of pipe fittings, valves and gauges"></div>
    <div class="brand-name">Kelvora</div>
    <p class="tagline">Supplying all your heating, cooling and hot water needs</p>
  </section>

  <section class="card card-back" aria-label="Business card back">
    <div class="card-pattern" role="img" aria-label="Faint repeating pattern of pipe fittings, valves and gauges"></div>
    <ul class="contact-list">
      <li class="contact-item">
        <span class="contact-icon">
          <svg width="22" height="22" viewBox="0 0 24 24" aria-hidden="true">
            <path fill="var(--icon-blue)" d="M6.6 10.8c1.4 2.8 3.8 5.1 6.6 6.6l2.2-2.2c.3-.3.7-.4 1-.2 1.1.4 2.3.6 3.6.6.6 0 1 .4 1 1V20c0 .6-.4 1-1 1C10.6 21 3 13.4 3 4c0-.6.4-1 1-1h3.5c.6 0 1 .4 1 1 0 1.3.2 2.5.6 3.6.1.3 0 .7-.2 1L6.6 10.8z"/>
          </svg>
        </span>
        <span class="contact-text">0438 615 247</span>
      </li>
      <li class="contact-item">
        <span class="contact-icon">
          <svg width="26" height="20" viewBox="0 0 26 20" aria-hidden="true">
            <rect x="1.5" y="2" width="23" height="16" fill="none" stroke="var(--icon-blue)" stroke-width="1.8"/>
            <path d="M1.5 2 L13 11 L24.5 2 M1.5 18 L10 9.5 M24.5 18 L16 9.5" fill="none" stroke="var(--icon-blue)" stroke-width="1.6"/>
          </svg>
        </span>
        <span class="contact-text">info@kelvoraplumbing.example.au</span>
      </li>
    </ul>
  </section>
</main>
</body>
</html>
```